8x14 Cardiology Testing Patient Education Brochure

We need an updated version of our existing testing brochure. The purpose of the brochure is to give patients information about their test: what the test is for, what will happen during the test, the duration of the test, and any preparation that is required.

The brochure should communicate professionalism, credibility, and dedication to patient care. It needs to be easy to read, with the test prep instructions particularly emphasized.

We want to stay with our current format: 8x14, parallel fold.

We are one practice with two different locations and office names.

Target Market(s)

male and female cardiology patients, 50+, 6th grade reading level

Industry/Entity Type

Medical Imaging

Font styles to use
Serif

Requirements
Must have
• The order of the content must be the same:
• 1. Locations and the Cardiac Testing Guide
• 2. Testing Services list
• 3. Services available at Ashford and Brookfield Offices
• 4. Services only at Ashford Office
• 5. Services only at Larkhaven Medical Center
• 6. How to Obtain Your Test Results
• Prep Instructions can go anywhere that makes sense layout wise, but need visual emphasis. If the patient doesn't follow the instructions we are unable to do the test so the prep is very important.
• our logos
• our red is pantone 207
• Remove 888-555-0148 from Ashford location contact information
• Change 540-555-0172 to 540-555-0139 on Ashford location contact information
Nice to have
• Illustrations or anatomic photos are great.
Should not have
• Stock cardiac imagery that involves people. Stock photos without people are fine.

```html
<!DOCTYPE html>
<html lang="en">
<head>
<meta charset="UTF-8">
<title>Cardiac Testing Patient Guide – Inside Spread</title>
<link href="https://fonts.googleapis.com/css2?family=Roboto+Condensed:wght@400;700&family=Montserrat:wght@700&display=swap" rel="stylesheet">
<style>
  :root{
    --crimson:#c1124f;
    --crimson-dark:#9e0c40;
    --ink:#2b2b2b;
    --black:#141414;
    --paper:#ffffff;
    --stage:#e4e5e8;
    --haze:#eef0f3;
  }
  *{box-sizing:border-box;margin:0;padding:0}
  html,body{width:1200px;height:800px;overflow:hidden;background:var(--stage)}
  body{font-family:"Roboto Condensed",Arial,sans-serif;color:var(--ink)}
  .spread{position:absolute;left:30px;top:28px;width:1140px;height:744px;display:flex;box-shadow:0 4px 18px rgba(0,0,0,.18)}
  .panel{position:relative;width:570px;height:100%;background:var(--paper);overflow:hidden}
  .panel--left{border-right:1px solid #d8d9dc}
  .panel__photo{position:absolute;left:150px;top:230px;width:300px;height:420px;
    background:radial-gradient(ellipse at center,#dcdfe5 0%,#eceef2 55%,rgba(255,255,255,0) 80%);opacity:.8}
  .panel--right .panel__photo{left:90px;top:80px;width:420px;height:520px}
  .corner{position:absolute;top:0}
  .panel--left .corner{left:0}
  .panel--right .corner{right:0}
  .banner{position:absolute;top:56px;height:46px;background:var(--crimson);color:#fff;
    font-weight:700;font-size:17px;line-height:19px;text-align:center;display:flex;align-items:center;justify-content:center}
  .panel--left .banner{left:110px;right:0;clip-path:polygon(4% 0,100% 0,100% 100%,0 100%)}
  .panel--right .banner{left:0;right:100px;top:40px;clip-path:polygon(0 0,100% 0,96% 100%,0 100%)}
  .service{position:absolute;width:250px}
  .service__title{display:table;margin:0 auto 8px;background:var(--crimson);color:#fff;font-weight:700;
    font-size:14px;line-height:16px;padding:5px 10px;text-align:center;box-shadow:2px 2px 0 rgba(0,0,0,.15)}
  .service__title--wide{text-align:left;margin:0 0 8px}
  .service p{font-size:9.6px;line-height:12.2px;text-align:justify;margin-bottom:6px}
  .service .notice{font-weight:700}
  .guide{position:absolute;left:300px;top:580px;width:240px}
  .guide__title{font-family:"Montserrat",Arial,sans-serif;color:var(--crimson);font-size:15px;line-height:17px;text-align:center;margin-bottom:6px}
  .guide__row{display:flex;font-size:11px;line-height:16px;color:var(--black)}
  .guide__row span{flex:none;margin-right:4px}
  .guide__row i{flex:1;border-bottom:1px solid var(--black);margin-bottom:4px}
</style>
</head>
<body>
<main class="spread">
  <section class="panel panel--left">
    <div class="panel__photo" role="img" aria-label="Faded photo of a cardiac testing room"></div>
    <svg class="corner" width="120" height="170" viewBox="0 0 120 170" aria-hidden="true">
      <path d="M0 30 L120 30 L120 74 Q42 74 30 130 L28 168 L0 168 Z" fill="var(--crimson)"/>
      <path d="M0 78 Q42 84 48 112 Q42 140 0 156 Z" fill="var(--black)"/>
    </svg>
    <h2 class="banner">Services Available at Ashford and<br>Brookfield Offices</h2>

    <article class="service" style="left:22px;top:188px">
      <h3 class="service__title">Nuclear Stress Test</h3>
      <p>This test uses a radioactive tracer to image the blood flow and strength of your heart muscle.</p>
      <p>After registration, a Certified Nuclear Medicine Technologist will prepare you for the test by starting an IV and injecting a small amount of nuclear tracer. There will be a delay of about 30 to 60 minutes to allow the tracer to be absorbed, before you are placed on the imaging table. You will lie on the table for 15 minutes while the camera takes pictures around your chest.</p>
      <p>Upon completion of the first set of pictures, you will be prepped for the stress portion of the test. If able to walk on treadmill this is preferred. If you are unable to walk on the treadmill, one of 2 medications called Cardivex or Dobutamine will be infused through an IV to complete the stress portion of your test. This medication will be determined by your doctor of the professional administering your test. Approximately 30-45 minutes after completing the treadmill or medication stress portion you will be placed on the imaging table for another 15 minute scan. Please allow 3 hours for the entire test. For 2 day tests, allow 90 minutes each day. See All STRESS Prep Instructions.</p>
      <p class="notice">*There is a charge for the radioactive tracer if you fail to give 24 hours notice to cancel the procedure.*</p>
    </article>

    <article class="service" style="left:22px;top:590px">
      <h3 class="service__title">Treadmill Stress Test</h3>
      <p>This test is used to detect EKG changes that occur when your heart is under stress. Several electrodes will be placed on your chest, so that your heart rhythm can be analyzed closely throughout the test.</p>
    </article>

    <article class="service" style="left:298px;top:150px">
      <h3 class="service__title">Venous Insufficiency</h3>
      <p>This test uses sound waves to determine the presence of leaks in the valves of the veins of the affected leg(s) or arm(s). While you lie on a table, a technologist will scan your leg(s) or arm(s) with an ultrasound probe. They will press down with the ultrasound probe from time to time to determine presence or absence of blood clots before they proceed to the insufficiency portion of the exam. There is no prep for this exam. This study typically last approximately 1 hr per leg or arm.</p>
    </article>

    <article class="service" style="left:298px;top:300px">
      <h3 class="service__title">Lower Extremity<br>Arterial Duplex (LEAD)</h3>
      <p>The study is used to evaluate the arteries that supply blood flow to your feet. While you lie on a table, a technologist will scan your legs with an ultrasound probe. There is no prep for this exam. The study typically lasts approximately 1/2 hour per leg.</p>
    </article>

    <article class="service" style="left:298px;top:430px">
      <h3 class="service__title">Holter / Event Monitors /<br>Mobile Telemetry</h3>
      <p>These monitors are used to analyze your heart rhythm over a period of time. The Holter Monitor is usually worn for 24-48 hours. The Event/Mobile Telemetry monitors are worn for 21-30 days.</p>
    </article>

    <article class="service" style="left:298px;top:560px">
      <h3 class="service__title">Echocardiogram</h3>
      <p>This test uses sound waves to take images of your heart muscle, heart valves, and other structures. You simply lie on your left side while a Sonographer scans your chest. There is no prep needed for this exam, which lasts approximately 45 minutes.</p>
    </article>
  </section>

  <section class="panel panel--right">
    <div class="panel__photo" role="img" aria-label="Faded photo of an ultrasound exam room"></div>
    <svg class="corner" width="110" height="200" viewBox="0 0 110 200" aria-hidden="true">
      <path d="M110 60 Q60 60 55 110 Q60 150 110 170 Z" fill="var(--black)"/>
      <path d="M0 20 L110 20 L110 60 Q50 60 40 84 L0 84 Z" fill="var(--crimson)"/>
    </svg>
    <h2 class="banner">Services Available Only at<br>Ashford Office</h2>

    <article class="service" style="left:22px;top:116px">
      <h3 class="service__title">Carotid Doppler</h3>
      <p>This exam uses sound waves to image the arteries that supply blood flow to your brain. You will lie on a table while a Sonographer scans your neck. There is no prep for this procedure, however, please avoid wearing perfumes or powders. This exam takes about 1 hour.</p>
    </article>

    <article class="service" style="left:22px;top:226px">
      <h3 class="service__title">Venous Study – DVT</h3>
      <p>This test uses sound waves to locate blood clots in the veins of the affected leg(s) or arm(s). While you lie on a table, a technologist will scan your leg(s) or arm(s) with an ultrasound probe. They will press down with the ultrasound probe from time to time to further determine presence or absence of blood clots. There is no prep for this exam. This study typically last approximately ½ hr per leg or arm.</p>
    </article>

    <article class="service" style="left:22px;top:360px">
      <h3 class="service__title">Renal Artery Doppler</h3>
      <p>This test uses sound waves to image the arteries that supply blood flow to your kidneys. You will lie on a table while a Sonographer scans your abdomen. The procedure lasts approximately 1 hour. See Vascular Prep Instructions.</p>
    </article>

    <article class="service" style="left:22px;top:460px">
      <h3 class="service__title">Abdominal Aortic<br>Aneurysm (AAA) Screening</h3>
      <p>This test uses ultrasound waves to image the main artery that supplies blood to and through your abdomen. You will lie on a table while a technologist scans your abdomen with an ultrasound probe. The procedure lasts 30-45 minutes. See Vascular Prep Instructions.</p>
    </article>

    <article class="service" style="left:22px;top:592px">
      <h3 class="service__title">Stress Echocardiogram</h3>
      <p>You will be required to walk a treadmill. This test uses Echocardiography (ultrasound) imaging to capture pictures of the heart at rest and with exercise to determine heart function. The entire test will take approximately 1 hour.</p>
    </article>

    <article class="service" style="left:300px;top:200px;width:240px">
      <h3 class="service__title service__title--wide">ERNA-Equilibrium Radio-<br>Nuclear Angiogram Scan<br>(MUGA)</h3>
      <p>This test uses an injected tracer to evaluate the wall motion of the heart. No prep is required. The test will last approximately 1 hour.</p>
    </article>

    <article class="service" style="left:300px;top:360px;width:240px">
      <h3 class="service__title service__title--wide">Pulse Volume Recording (PVR)<br>Ankle-Brachial Index (ABI)</h3>
      <p>These are exams performed to evaluate the amount of blood flowing to your arms and legs. A series of blood pressure cuffs are applied to obtain pressures and tracings. There is no other prep for these exams. PVR will take approxi-mately 1 hour and the ABI takes about 15 minutes.</p>
    </article>

    <div class="guide">
      <h2 class="guide__title">Patient Guide and<br>Prep Instructions</h2>
      <div class="guide__row"><span>Referred By:</span><i></i></div>
      <div class="guide__row"><span>Patient Name:</span><i></i></div>
      <div class="guide__row"><span>Test Date/Time:</span><i></i></div>
    </div>
  </section>
</main>
</body>
</html>
```